7 3/4 x 5 1/4 Annual Banquet Invitation

Design an invitation for our Chamber's annual banquet. It will be a single sided invitation 5 1/4" wide by 7 3/4" height that we will print in-house. Our logo is attached. The theme is "Serving Together". I was thinking of an image with two hands coming together in a handshake, perhaps intertwining our logo colors. This is just a thought. I am open for any suggestions! Text for the invitation should be as follows: The Board of Directors and Staff cordially invites you to attend the 64th Yearly Gathering & Micro-Trade Fair - Monday, January 22, 2018. 5:30 p.m. Social, 6:00 p.m. Dinner. Cedarvale Chapel, 4819 Harlan P. Moss Rd S, Ashbrook. Please RSVP by January 18, 2018.

Target Market(s)

This invitation will be printed and mailed to our membership.

Industry/Entity Type

Business Management

Colors
33a6d7
faa54b
0355a3
00a990

Requirements
Must have
• Event info as indentified above.
Nice to have
• Our Logo

```html
<!DOCTYPE html>
<html lang="en">
<head>
<meta charset="utf-8">
<title>64th Yearly Gathering Invitation</title>
<link rel="stylesheet" href="https://fonts.googleapis.com/css2?family=EB+Garamond:ital,wght@0,400;0,500;1,400&family=PT+Sans:wght@400;700&display=swap">
<style>
  :root {
    --backdrop: #dcdbd9;
    --card: #f3b955;
    --ornament: #d6a66c;
    --ink: #2b2113;
    --serif-ink: #241a0e;
    --blue: #2f63a8;
    --blue-soft: #4f6a95;
    --white: #ffffff;
    --teal: #33a6d7;
    --photo-light: #f4f3f0;
    --photo-mid: #c9c8c4;
  }
  * { margin: 0; padding: 0; box-sizing: border-box; }
  html, body {
    width: 1200px;
    height: 817px;
    overflow: hidden;
    background: var(--backdrop);
  }
  .stage {
    position: relative;
    width: 1200px;
    height: 817px;
  }
  .invitation {
    position: absolute;
    left: 418px;
    top: 203px;
    width: 345px;
    height: 484px;
    background: var(--card);
    font-family: "PT Sans", sans-serif;
    color: var(--ink);
  }
  .top-ornament {
    position: absolute;
    left: 7px;
    top: 4px;
    width: 330px;
    height: 16px;
    border-radius: 8px;
    background: linear-gradient(90deg, rgba(214,166,108,0.3), var(--ornament) 20%, var(--ornament) 80%, rgba(214,166,108,0.3));
  }
  .chamber-mark {
    position: absolute;
    left: 44px;
    top: 44px;
    display: flex;
    flex-direction: column;
    align-items: center;
    gap: 3px;
  }
  .chamber-mark .dot {
    width: 12px;
    height: 12px;
    border-radius: 50%;
    background: var(--teal);
  }
  .chamber-mark .name {
    font-size: 5.5px;
    font-weight: 700;
    letter-spacing: 0.2px;
    color: var(--blue);
    text-transform: uppercase;
  }
  .host-line {
    position: absolute;
    left: 45px;
    top: 78px;
    font-size: 9.5px;
    line-height: 12px;
    color: var(--ink);
  }
  .edition {
    position: absolute;
    left: 186px;
    top: 62px;
    font-size: 40px;
    font-weight: 400;
    line-height: 1;
    color: var(--white);
  }
  .edition sup {
    font-size: 18px;
    vertical-align: top;
    position: relative;
    top: 2px;
    margin-left: 2px;
  }
  .event-title {
    position: absolute;
    left: 45px;
    top: 106px;
    font-family: "EB Garamond", serif;
    font-style: italic;
    font-weight: 400;
    font-size: 29px;
    line-height: 1;
    color: var(--blue);
  }
  .event-subtitle {
    position: absolute;
    left: 45px;
    top: 138px;
    font-family: "EB Garamond", serif;
    font-style: italic;
    font-size: 18px;
    line-height: 1;
    color: var(--blue-soft);
  }
  .big-letter {
    position: absolute;
    left: 0;
    top: 172px;
    width: 345px;
    height: 45px;
    overflow: hidden;
  }
  .big-letter text {
    font-family: "EB Garamond", serif;
    font-size: 236px;
    fill: var(--serif-ink);
  }
  .hands-photo {
    position: absolute;
    left: 45px;
    top: 217px;
    width: 147px;
    height: 160px;
    background: radial-gradient(ellipse at 50% 55%, var(--photo-light) 30%, var(--photo-mid) 100%);
  }
  .word-part {
    position: absolute;
    top: 290px;
    font-family: "EB Garamond", serif;
    font-weight: 400;
    font-size: 30px;
    line-height: 1;
    color: var(--serif-ink);
  }
  .word-part.lead { left: 4px; }
  .word-part.tail { left: 194px; }
  .details {
    position: absolute;
    left: 45px;
    top: 381px;
    width: 200px;
    color: var(--ink);
  }
  .details .when {
    font-size: 11.5px;
    line-height: 17px;
  }
  .details .where {
    font-size: 10px;
    line-height: 16px;
  }
  .details .rsvp {
    font-size: 8.5px;
    line-height: 12px;
  }
</style>
</head>
<body>
<div class="stage">
  <article class="invitation">
    <div class="top-ornament" role="img" aria-label="Decorative scroll flourish"></div>

    <div class="chamber-mark">
      <span class="dot"></span>
      <span class="name">Harborview Chamber</span>
    </div>

    <p class="host-line">The Board of Directors and Staff<br>cordially invites you to attend the</p>
    <p class="edition">64<sup>th</sup></p>
    <h1 class="event-title">Yearly Gathering</h1>
    <p class="event-subtitle">&amp; Micro-Trade Fair</p>

    <svg class="big-letter" viewBox="0 0 345 45" aria-hidden="true">
      <text x="117" y="153" text-anchor="middle">V</text>
    </svg>

    <div class="hands-photo" role="img" aria-label="Black and white photo of two hands clasped together"></div>

    <h2 class="word-part lead" aria-label="Invitation">IN</h2>
    <span class="word-part tail" aria-hidden="true">ITATION</span>

    <div class="details">
      <p class="when">Monday, January 22, 2018.<br>5:30 p.m, Social, 6:00 p.m<br>Dinner.</p>
      <p class="where">Cedarvale Chapel, 4819 Harlan<br>P. Moss Rd S, Ashbrook.</p>
      <p class="rsvp">Please RSVP by January 18, 2018</p>
    </div>
  </article>
</div>
</body>
</html>
```